Naturopath Practitioner Card Design

I am a naturopath needing a design for a business card mainly to show that I am a naturopath and have some contact details to give to prospective clients. I am open minded about the design and what is on the second side of the card whether it just be some artwork or space for details, appointment times etc. Naturopathy is the practice of natural medicine that uses a holistic approach and incorporates herbal and nutritional medicine.

Industry/Entity Type

Business

Contact Information for Business Card

Tom Welby NaturopathBHSc (Naturopathy) Member PHRA 0492 815 306 tom.welby@mailbright.com www.tomwelbynaturopathy.com.au

Requirements
Nice to have
• Would prefer some kind of original pattern/art work/logo rather than an image, not fussed if its very simple/basic
• I am open to any colour but think I would prefer a more earthy sandy clay etc type style than the greens that are commonly associated with naturopathy.
Should not have
• Don't really want to have generic stock images on it

```html
<!DOCTYPE html>
<html lang="en">
<head>
<meta charset="utf-8">
<title>Tom Welby – Naturopath Business Card</title>
<link rel="stylesheet" href="https://fonts.googleapis.com/css2?family=Source+Sans+3:ital,wght@0,400;0,600;0,700;1,700&display=swap">
<style>
  :root {
    --page-bg: #ecebe8;
    --card-bg: #ffffff;
    --leaf-deep: #3f8f12;
    --leaf-mid: #7cc21f;
    --leaf-light: #c9ec8a;
    --leaf-glow: #f2fbe4;
    --brand-green: #4aa414;
    --text-grey: #4a4a4a;
    --rule-rose: #f08a8f;
    --note-navy: #1d2540;
    --card-shadow: rgba(0, 0, 0, 0.18);
  }
  * { box-sizing: border-box; margin: 0; padding: 0; }
  html, body {
    width: 1200px; height: 900px; overflow: hidden;
    background: var(--page-bg);
    font-family: "Source Sans 3", "Myriad Pro", Arial, sans-serif;
  }
  .stage { position: relative; width: 1200px; height: 900px; }

  .card {
    position: absolute;
    background: var(--card-bg);
    overflow: hidden;
    box-shadow: 0 6px 18px var(--card-shadow);
  }
  .card--front { left: 238px; top: 62px; width: 556px; height: 342px; }
  .card--back  { left: 457px; top: 518px; width: 561px; height: 343px; }

  .foliage {
    position: absolute; left: 0; top: 0; width: 100%; height: 72%;
    background:
      radial-gradient(ellipse 16% 30% at 5% 12%, var(--leaf-deep), transparent 70%),
      radial-gradient(ellipse 22% 42% at 92% 22%, var(--leaf-deep), transparent 70%),
      radial-gradient(ellipse 30% 35% at 62% 18%, var(--leaf-glow), transparent 75%),
      radial-gradient(ellipse 45% 55% at 30% 25%, var(--leaf-mid), transparent 80%),
      linear-gradient(180deg, var(--leaf-mid) 0%, var(--leaf-light) 45%, rgba(255,255,255,0) 100%);
  }

  .centered {
    position: absolute; left: 0; width: 100%;
    text-align: center; transform: translateY(-50%);
  }
  .name {
    color: var(--brand-green); font-weight: 700; font-size: 19px;
  }
  .role, .credentials {
    color: var(--text-grey); font-size: 15px;
  }
  .contact {
    position: absolute; transform: translateY(-50%);
    display: flex; align-items: center; gap: 8px;
    color: var(--text-grey); font-size: 15px;
  }
  .contact svg { width: 11px; height: 11px; fill: var(--brand-green); }
  .contact--phone { left: 210px; top: 273px; }
  .contact--email { left: 176px; top: 293px; }

  .appointment-title {
    color: var(--brand-green); font-weight: 600; font-size: 23px;
  }
  .field-label {
    position: absolute; transform: translateY(-50%);
    color: var(--note-navy); font-size: 15px;
  }
  .field-rule {
    position: absolute; height: 1px; background: var(--rule-rose);
  }
  .notice {
    color: var(--note-navy); font-style: italic; font-weight: 700; font-size: 15px;
  }
</style>
</head>
<body>
<main class="stage">

  <section class="card card--front" aria-label="Business card front">
    <div class="foliage" role="img" aria-label="Sunlit green leaves photograph"></div>
    <h1 class="centered name" style="top:184px">Tom Welby</h1>
    <p class="centered role" style="top:206px">Naturopath</p>
    <p class="centered credentials" style="top:232px">BHSc (Naturopathy) Member PHRA</p>
    <p class="contact contact--phone">
      <svg viewBox="0 0 24 24" aria-hidden="true"><path d="M6.6 10.8a15.1 15.1 0 0 0 6.6 6.6l2.2-2.2c.3-.3.7-.4 1-.2 1.1.4 2.3.6 3.6.6.6 0 1 .4 1 1V20c0 .6-.4 1-1 1A17 17 0 0 1 3 4c0-.6.4-1 1-1h3.5c.6 0 1 .4 1 1 0 1.3.2 2.5.6 3.6.1.3 0 .7-.2 1z"/></svg>
      0492 815 306
    </p>
    <p class="contact contact--email">
      <svg viewBox="0 0 24 24" aria-hidden="true"><path d="M2 5h20v14H2z M2 5l10 7 10-7" /></svg>
      tom.welby@mailbright.com
    </p>
  </section>

  <section class="card card--back" aria-label="Business card back: appointment reminder">
    <div class="foliage" role="img" aria-label="Sunlit green leaves photograph"></div>
    <h2 class="centered appointment-title" style="top:169px">Your Next Appointment is</h2>

    <span class="field-label" style="left:82px; top:211px">Name :</span>
    <span class="field-rule" style="left:141px; top:215px; width:322px"></span>

    <span class="field-label" style="left:82px; top:251px">Date :</span>
    <span class="field-rule" style="left:140px; top:253px; width:323px"></span>

    <span class="field-label" style="left:85px; top:284px">Time:</span>
    <span class="field-rule" style="left:143px; top:288px; width:108px"></span>
    <span class="field-label" style="left:258px; top:284px">AM</span>
    <span class="field-rule" style="left:295px; top:288px; width:151px"></span>
    <span class="field-label" style="left:455px; top:284px">PM</span>

    <p class="centered notice" style="top:318px">If unable to keep appointment, kindly give 24hrs notice.</p>
  </section>

</main>
</body>
</html>
```